New furniture company needs a cool, fresh Website - think lounjo.com, velmora.com

Quiltrest.com: We are launching a home (storefront) furniture business, aimed at the young, discerning mid-market consumer. The aim is to compete with many furniture e-tailers, as well as more established retail brands.
We want the website to capture the hearts, minds and wallets of the target audience, placing Quiltrest.com firmly into the market place. Please look to Velmora.com for look and feel inspiration. We will be selling approx 15 products to start. I suggest using storefront with the following theme please: – Hearth & Meadow – Cadenza – Ravel. Please see the logo below. The website needs to have a sophisticated feel for affordable aspirational furniture. Soft colours and homely text - please go with look and feel of Velmora.com. Please see a below file containing image of some sofas, chairs and footstools that will be for sale.
Many thanks

Target Market(s)

mid-market, young families looking for cool, affordable, easy to buy furniture

Industry/Entity Type

Furniture

Coding

Coded - Design and coding required

Number of Pages Required

5+ page

Font styles to use
Sans Serif

Colors
86cae7
cee9f5
3277b5
eaf2ce
fdf9ce
fff3d1
0255a3
e8e8e8
cbcbcb

Requirements
Must have
• storefront
• http://www.velmora.com/hartwick-leather-large-sofa.html - great example of what we need it to look like
• logo as shown
• homepage
• products menu - sofas, seating, footstools, antique
• images of all products (examples provided) with ability to click on various fabric swatch samples and see the sofa in different fabrics and colours (check out lounjo.com)
• facility for social media
• facility to buy online
• "add to wishlist"
• "add to basket"
Nice to have
• I want it to have a light and airy feel, nothing too heavy or corporate. Needs to be very easily navigated and a simple approach
Should not have
• Dark, heavy colours

```html
<!DOCTYPE html>
<html lang="en">
<head>
<meta charset="utf-8">
<title>Quiltrest – Home</title>
<link href="https://fonts.googleapis.com/css2?family=Lato:wght@300;400;700&display=swap" rel="stylesheet">
<style>
:root{
  --blue:#0255a3;
  --blue-mid:#3277b5;
  --mint:#eaf2ce;
  --grey-light:#e8e8e8;
  --grey:#cbcbcb;
  --text:#333;
  --muted:#888;
  --white:#fff;
}
*{box-sizing:border-box;margin:0;padding:0}
html,body{width:802px;height:1200px;overflow:hidden;background:var(--white);font-family:'Lato',sans-serif;color:var(--text)}
.page{position:relative;width:802px;height:1200px}
.abs{position:absolute}
.wrap{left:126px;width:553px}

/* header */
.logo{left:126px;top:16px;width:82px;text-align:center}
.logo-mark{width:18px;height:18px;border:1.5px solid #777;border-radius:50%;margin:0 auto 7px}
.logo-name{font-size:9px;letter-spacing:2.5px;color:#666}
.util{right:123px;top:13px;font-size:6.5px;color:var(--muted);display:flex;gap:6px;align-items:center}
.util .sep{color:var(--grey)}
.search{left:538px;top:37px;width:141px;height:20px;border:1px solid var(--grey);border-radius:10px;font-size:6.5px;color:#aaa;display:flex;align-items:center;padding-left:10px;gap:6px}

/* nav */
.nav{top:71px;height:24px;border-top:2px solid var(--grey-light);border-bottom:1px solid var(--grey-light);display:flex;align-items:center;font-size:7.5px;color:var(--muted)}
.nav a{color:inherit;text-decoration:none;margin-left:7px;width:75px}
.nav .cat{margin-left:auto;height:21px;width:101px;background:var(--grey);color:var(--white);display:flex;align-items:center;gap:6px;padding-left:7px;font-size:8.5px}

/* hero */
.hero{top:102px;height:220px;display:flex}
.hero-copy{width:200px;background:var(--mint);position:relative}
.hero-copy .line{position:absolute;height:1px;background:#333}
.hero-big{position:absolute;left:22px;top:74px;font-size:34px;font-weight:400;color:var(--blue-mid);letter-spacing:.5px}
.hero-small{position:absolute;left:22px;top:115px;font-size:22px;font-weight:300;color:#222}
.hero-photo{flex:1;position:relative;background:
  linear-gradient(180deg,#5f5d5a 0%,#6c6a66 30%,#9a9a96 52%,#b4b4b0 66%,#8e8d89 82%,#55524e 100%)}
.arrows{position:absolute;right:4px;bottom:2px;display:flex;gap:2px}
.arrows span{width:17px;height:16px;background:#333;color:#fff;font-size:10px;display:flex;align-items:center;justify-content:center}

/* promos */
.promos{top:330px;height:125px;display:flex;justify-content:space-between}
.promo{width:180px;position:relative}
.promo .tag{position:absolute;left:0;top:94px;height:22px;padding:0 8px;font-size:10px;display:flex;align-items:center}
.p1{background:linear-gradient(180deg,#4d4944 0%,#5a4a44 35%,#7d1e22 50%,#8a2a2a 68%,#a89272 100%)}
.p2{background:linear-gradient(180deg,#b8aa92 0%,#a7a095 35%,#9c9a95 55%,#8d8983 75%,#6a655d 100%)}
.p3{background:linear-gradient(180deg,#6e6c65 0%,#8e8b84 30%,#d2cfc7 52%,#c5c1b9 70%,#8a867e 100%)}
.p1 .tag{background:var(--blue);color:#fff}
.p2 .tag{background:var(--mint);color:#222}
.p3 .tag{background:#eee;color:#222}

/* section headings */
.sec-head{height:22px;border-top:1px solid var(--grey-light);border-bottom:1px solid var(--grey-light);font-size:10.5px;display:flex;align-items:center;padding-left:6px}
.sec-head .ctrl{margin-left:auto;display:flex;gap:3px}
.sec-head .ctrl span{width:17px;height:15px;background:var(--grey);color:#fff;font-size:9px;display:flex;align-items:center;justify-content:center}

/* products */
.products{top:526px;display:flex;justify-content:space-between}
.card{width:135px;text-align:center;border-bottom:3px solid var(--grey-light);padding-bottom:10px}
.card .shot{height:112px;border:1px solid var(--grey-light);padding:14px}
.card .shot div{width:100%;height:100%;border-radius:3px}
.s1 div{background:linear-gradient(180deg,#f4f1e8 0%,#e6e1d1 45%,#d6cfbb 80%,#f3f1ea 100%)}
.s2 div{background:linear-gradient(180deg,#efe5d2 0%,#e2d3b8 55%,#c9b89b 78%,#6a4a3a 100%)}
.s3 div{background:linear-gradient(180deg,#f2f2f4 0%,#4a4852 40%,#2c2a33 70%,#ecebef 100%)}
.s4 div{background:linear-gradient(180deg,#efe7da 0%,#cdb99a 40%,#bfae95 60%,#ddd8ce 80%,#f1efea 100%)}
.card .name{font-size:8.5px;margin-top:12px}
.card .price{font-size:8px;color:#555;margin-top:3px}
.card .price b{color:var(--blue);font-weight:700}
.card .buy{display:inline-block;margin-top:7px;width:57px;height:16px;line-height:14px;border:1px solid var(--blue-mid);border-radius:2px;color:var(--blue);font-size:7px;font-weight:700}

/* gallery */
.gallery{top:777px;height:235px;display:grid;grid-template-columns:179px 184px 180px;grid-template-rows:139px 92px;gap:4px 5px}
.g1{background:#444;padding:5px}
.g1 .inner{height:100%;border:1px solid #666;background:linear-gradient(180deg,#3a3a3a 0%,#1a1a1a 35%,#0e0e0e 70%,#3a3a3a 100%);display:flex;flex-direction:column;align-items:center;justify-content:center;color:#fff;font-size:11px;gap:6px}
.g1 .icons{display:flex;gap:3px}
.g1 .icons span{width:17px;height:17px;border:1px solid #fff;border-radius:50%}
.g2{grid-row:1/3;grid-column:2;background:linear-gradient(180deg,#e8e8e8 0%,#e4dfcc 35%,#ddd4b9 60%,#c9bfa6 78%,#e8e8e8 100%)}
.g3{grid-column:3;background:linear-gradient(180deg,#e8e8e8 0%,#a5ae9f 35%,#7f8a7c 65%,#e8e8e8 100%)}
.g4{grid-column:1;grid-row:2;background:linear-gradient(180deg,#e8e8e8 0%,#e7ddd2 35%,#d9cdbf 70%,#e8e8e8 100%)}
.g5{grid-column:3;grid-row:2;background:linear-gradient(180deg,#e8e8e8 0%,#98805f 30%,#7a6446 70%,#e8e8e8 100%)}

/* footer */
.foot{top:1042px;height:128px;border-top:2px solid var(--grey-light);border-bottom:2px solid var(--grey-light)}
.col{position:absolute;top:20px}
.col h3{font-size:10.5px;font-weight:400;margin-bottom:10px}
.contact-item{display:flex;gap:6px;font-size:6.5px;color:#666;margin-bottom:9px;line-height:1.3}
.contact-item svg{flex:none}
.links li{list-style:none;font-size:7px;color:var(--muted);margin-bottom:8px;display:flex;align-items:center;gap:5px}
.links li::before{content:"";width:4px;height:4px;border:1px solid #aaa;transform:rotate(45deg)}
.social li{list-style:none;font-size:7px;color:var(--muted);margin-bottom:6px;display:flex;align-items:center;gap:7px}
.social li span{width:14px;height:14px;border:1px solid var(--grey);border-radius:50%}
.news input{display:block;border:0;border-bottom:1px solid var(--grey);width:140px;font-family:inherit;font-size:7px;color:#999;padding:3px 0 7px;background:none}
.news .submit{margin-top:10px;width:60px;height:16px;border:1px solid var(--grey);font-size:7px;color:#aaa;display:flex;align-items:center;justify-content:center}
.copy{top:1184px;left:0;width:802px;text-align:center;font-size:6px;color:var(--muted)}
</style>
</head>
<body>
<div class="page">

  <header>
    <div class="abs logo">
      <div class="logo-mark"></div>
      <div class="logo-name">QUILTREST</div>
    </div>
    <div class="abs util">
      <span>My Account</span><span class="sep">|</span>
      <span>Basket (0)</span><span class="sep">|</span>
      <span>storefront</span>
    </div>
    <div class="abs search">
      <svg width="8" height="8" viewBox="0 0 10 10"><circle cx="4" cy="4" r="3" fill="none" stroke="#999" stroke-width="1.2"/><line x1="6.3" y1="6.3" x2="9" y2="9" stroke="#999" stroke-width="1.2"/></svg>
      Search Product
    </div>
    <nav class="abs wrap nav">
      <a>Home</a><a>About Us</a><a>Products</a><a>Gallery</a><a>Contact Us</a>
      <div class="cat">
        <svg width="12" height="8" viewBox="0 0 12 8"><path d="M0 1h12M0 4h12M0 7h12" stroke="#fff" stroke-width="1"/></svg>
        Product Category
      </div>
    </nav>
  </header>

  <section class="abs wrap hero">
    <div class="hero-copy">
      <div class="line" style="left:12px;top:73px;width:63px"></div>
      <div class="hero-big">20 % OFF</div>
      <div class="hero-small">ON THIS SOFA</div>
      <div class="line" style="left:122px;top:148px;width:64px"></div>
      <div class="line" style="left:136px;top:151px;width:30px"></div>
    </div>
    <div class="hero-photo" role="img" aria-label="Grey upholstered three-seat sofa against a stone wall">
      <div class="arrows"><span>‹</span><span>›</span></div>
    </div>
  </section>

  <section class="abs wrap promos">
    <div class="promo p1" role="img" aria-label="Red velvet buttoned sofa"><div class="tag">Save 10 % on this Sofa</div></div>
    <div class="promo p2" role="img" aria-label="Grey fabric sofa with cushions"><div class="tag">Save 15 % on this Sofa</div></div>
    <div class="promo p3" role="img" aria-label="Light buttoned-back sofa"><div class="tag">Save 20 % on this Sofa</div></div>
  </section>

  <div class="abs wrap sec-head" style="top:491px">Feature Products
    <div class="ctrl"><span>‹</span><span>›</span></div>
  </div>

  <section class="abs wrap products">
    <div class="card"><div class="shot s1" role="img" aria-label="Cream two-seat sofa"><div></div></div><div class="name">Product Name Here</div><div class="price">Price : <b>£ 1,885</b></div><div class="buy">Buy Now</div></div>
    <div class="card"><div class="shot s2" role="img" aria-label="Buttoned wingback accent chair"><div></div></div><div class="name">Product Name Here</div><div class="price">Price : <b>£ 1,885</b></div><div class="buy">Buy Now</div></div>
    <div class="card"><div class="shot s3" role="img" aria-label="Dark chaise longue"><div></div></div><div class="name">Product Name Here</div><div class="price">Price : <b>£ 1,885</b></div><div class="buy">Buy Now</div></div>
    <div class="card"><div class="shot s4" role="img" aria-label="Upholstered footstool with tray"><div></div></div><div class="name">Product Name Here</div><div class="price">Price : <b>£ 1,885</b></div><div class="buy">Buy Now</div></div>
  </section>

  <div class="abs wrap sec-head" style="top:743px;padding-left:14px">Photo Gallery</div>

  <section class="abs wrap gallery">
    <div class="g1" role="img" aria-label="Black buttoned footstool">
      <div class="inner">Product name Here<div class="icons"><span></span><span></span></div></div>
    </div>
    <div class="g2" role="img" aria-label="Cream buttoned armless chair"></div>
    <div class="g3" role="img" aria-label="Sage green lounge chair"></div>
    <div class="g4" role="img" aria-label="Cream club armchair"></div>
    <div class="g5" role="img" aria-label="Brown velvet slipper chair"></div>
  </section>

  <footer class="abs wrap foot">
    <div class="col" style="left:0">
      <h3>Contact Us</h3>
      <div class="contact-item"><svg width="10" height="14" viewBox="0 0 10 14"><rect x="1" y="1" width="8" height="12" rx="1" fill="none" stroke="#999"/></svg><div>Call Us<br>(800)5550134297</div></div>
      <div class="contact-item"><svg width="10" height="14" viewBox="0 0 10 14"><rect x="1" y="1" width="8" height="12" rx="1" fill="none" stroke="#999"/></svg><div>Email<br>support@quiltrest.com</div></div>
      <div class="contact-item"><svg width="10" height="14" viewBox="0 0 10 14"><path d="M5 13C2 8 1 6.5 1 5a4 4 0 018 0c0 1.5-1 3-4 8z" fill="#999"/><circle cx="5" cy="5" r="1.5" fill="#fff"/></svg><div>Location<br>Lorem Ipsum is simply dumm</div></div>
    </div>
    <div class="col" style="left:167px">
      <h3>User Link</h3>
      <ul class="links"><li>Home</li><li>About Us</li><li>Products</li><li>Gallery</li><li>Contact Us</li></ul>
    </div>
    <div class="col" style="left:287px">
      <h3>Follow Us on</h3>
      <ul class="social"><li><span></span>Friendbook</li><li><span></span>Chirper</li><li><span></span>Vidtube</li><li><span></span>Circles+</li></ul>
    </div>
    <div class="col news" style="left:413px">
      <h3>Sign up for Newsletter</h3>
      <input type="text" value="Enter Email Address" readonly>
      <div class="submit">Submit</div>
    </div>
  </footer>

  <div class="abs copy">Copyright 2017. Quiltrest 2017 All rights reserved.</div>
</div>
</body>
</html>
```